Hand sanitizer logos and bottle design

Want a very simple and clean logo for - PURA42.
Need a badge logo for - Clean Shield 42 Keeper.
Need bottle label designed. Mock up is attached. Keep it very clean as in mockup.
Target Market(s)
retail
Font styles to use
Sans Serif
Requirements
Must have
- Simple Clean

```html
<!DOCTYPE html>
<html lang="en">
<head>
<meta charset="utf-8">
<title>PURA42 Gel Hand Sanitizer Label</title>
<link rel="stylesheet" href="https://fonts.googleapis.com/css2?family=Roboto:wght@400;500;700&family=Roboto+Condensed:wght@700&family=Archivo+Black&display=swap">
<style>
  :root {
    --backdrop: #b1b4b5;
    --label: #ffffff;
    --ink: #111111;
    --orange: #f58025;
    --blue: #1e9ad6;
    --blue-deep: #0a6fae;
  }
  html, body {
    margin: 0;
    padding: 0;
    width: 1200px;
    height: 1200px;
    overflow: hidden;
    background: var(--backdrop);
  }
  .label {
    position: absolute;
    left: 390px;
    top: 281px;
    width: 442px;
    height: 653px;
    overflow: hidden;
    background: var(--label);
    color: var(--ink);
    font-family: "Roboto", Arial, sans-serif;
  }
  .label > * { position: absolute; margin: 0; }
  .brand-name {
    left: 38px;
    top: 40px;
    width: 362px;
    height: 100px;
    overflow: visible;
  }
  .brand-name text {
    font-family: "Roboto", Arial, sans-serif;
    font-weight: 500;
    font-size: 115px;
    fill: var(--orange);
  }
  .brand-rule {
    left: 38px;
    top: 151px;
    width: 362px;
    height: 3px;
    background: var(--orange);
  }
  .headline {
    left: 38px;
    top: 160px;
    width: 362px;
    font-family: "Roboto Condensed", Arial, sans-serif;
    font-weight: 700;
    font-size: 39px;
    line-height: 1.1;
    white-space: nowrap;
    display: flex;
    justify-content: space-between;
  }
  .claim {
    left: 0;
    top: 206px;
    width: 436px;
    text-align: center;
    line-height: 1;
  }
  .claim-intro { display: block; font-size: 19px; }
  .claim-main {
    display: block;
    font-family: "Roboto Condensed", Arial, sans-serif;
    font-weight: 700;
    font-size: 39px;
    margin-top: 4px;
  }
  .claim-outro { display: block; font-size: 17.5px; margin-top: 8px; }
  .product-type {
    left: 40px;
    top: 355px;
    font-family: "Archivo Black", Arial, sans-serif;
    font-size: 25px;
    line-height: 28px;
    letter-spacing: 1.5px;
    text-transform: uppercase;
    white-space: nowrap;
  }
  .keeper-badge {
    left: 222px;
    top: 306px;
    width: 190px;
    height: 140px;
    display: flex;
    align-items: center;
    gap: 8px;
  }
  .keeper-badge-dot {
    flex: none;
    width: 46px;
    height: 46px;
    border-radius: 50%;
    background: var(--blue);
  }
  .keeper-badge-name {
    font-family: "Roboto", Arial, sans-serif;
    font-weight: 700;
    font-size: 20px;
    line-height: 1.1;
    color: var(--blue-deep);
    text-transform: uppercase;
  }
  .features {
    left: 37px;
    top: 445px;
    padding: 0;
    list-style: none;
    font-size: 23.5px;
    line-height: 31px;
    white-space: nowrap;
  }
  .cert-mark {
    left: 279px;
    top: 454px;
    width: 62px;
    height: 40px;
    border: 3px solid var(--ink);
    border-radius: 4px;
    box-sizing: border-box;
  }
  .net-content {
    left: 142px;
    top: 584px;
    display: flex;
    align-items: flex-end;
    gap: 8px;
  }
  .net-content-tag {
    font-size: 11px;
    line-height: 11px;
    text-align: center;
  }
  .net-content-tag span { display: block; }
  .net-content-tag span + span { font-size: 14px; line-height: 14px; }
  .net-content-volume { font-size: 31px; line-height: 0.85; }
</style>
</head>
<body>
  <main class="label">
    <svg class="brand-name" viewBox="0 0 362 100" role="img" aria-label="PURA42">
      <text x="0" y="95" textLength="362" lengthAdjust="spacingAndGlyphs">PURA42</text>
    </svg>
    <div class="brand-rule"></div>
    <p class="headline"><span>12</span><span>HOUR</span><span>PROTECTION</span></p>
    <p class="claim">
      <span class="claim-intro">Nanotechnology enables one use</span>
      <span class="claim-main">12 Hour protection</span>
      <span class="claim-outro">that will not dry out your skin</span>
    </p>
    <p class="product-type">Gel Hand<br>Sanitizer</p>
    <div class="keeper-badge">
      <span class="keeper-badge-dot"></span>
      <span class="keeper-badge-name">Clean Shield 42 Keeper</span>
    </div>
    <ul class="features">
      <li>Non Toxic</li>
      <li>Alchohol Free</li>
      <li>Extended Protection</li>
      <li>Kills 99.99% Viruses</li>
    </ul>
    <div class="cert-mark" role="img" aria-label="Certification badge"></div>
    <p class="net-content">
      <span class="net-content-tag"><span>CONT.</span><span>NET</span></span>
      <span class="net-content-volume">500 ML.</span>
    </p>
  </main>
</body>
</html>
```